Designing business cards for my start-up business

The company is called Pellion. We are a start-up tech data company based in Guernsey, Channel Islands. We want the business cards to look clean, fresh and innovative, just what a tech company should be. We do not want the business cards to look corporate or too official such as a bank. I would like the front of the business card to have our logo and the tag line of "Linking People". On the back will be our contact details, emails etc. However I am open to your ideas and suggestions. I have provided all our logos and a word doc of all our contact details. There are 4 directors of the business, so I want 4 versions of the same design.

Target Market(s)

Our clients are businesses of all industries. Its a broad target market.

Industry/Entity Type

Information Technology

Contact Information for Business Card

I have attached a word doc called "Business Cards info" which gives all contact details of the 4 employees for the company.

Requirements
Must have
• We must have our logo and the tag line of "Linking People". This could on the front of the card and then the individuals contact details on the back. Other than that, I'm happy for the designers to come up with ideas/styles.
Nice to have
• N/A
Should not have
• I don't want the cards to look too formal or corporate. As mentioned, we are a tech start-up so we want to look innovative.

```html
<!DOCTYPE html>
<html lang="en">
<head>
<meta charset="utf-8">
<title>Pellion business cards</title>
<link href="https://fonts.googleapis.com/css2?family=Open+Sans:ital,wght@0,400;0,600;0,700;1,400&display=swap" rel="stylesheet">
<style>
  :root {
    --page: #e9e7e3;
    --card: #ffffff;
    --orange: #ef5a3a;
    --orange-deep: #e2482c;
    --ink: #1f1f1f;
    --grey: #555555;
    --white: #ffffff;
  }
  * { box-sizing: border-box; margin: 0; padding: 0; }
  html, body {
    width: 1200px; height: 950px; overflow: hidden;
    background: var(--page);
    font-family: "Open Sans", Arial, sans-serif;
  }
  .canvas { position: relative; width: 1200px; height: 950px; }

  .card {
    position: absolute;
    width: 580px; height: 332px;
    background: var(--card);
    box-shadow: 0 6px 18px rgba(0,0,0,0.18);
    overflow: hidden;
  }
  .card--contact { left: 310px; top: 100px; }
  .card--brand { left: 310px; top: 518px; }

  /* contact side */
  .corner-tab {
    position: absolute; top: 0; right: 0;
    width: 26px; height: 10px; background: var(--orange);
  }
  .person { position: absolute; top: 26px; right: 34px; text-align: right; }
  .person__name { color: var(--orange); font-weight: 700; font-size: 19px; line-height: 1.2; }
  .person__role { color: var(--ink); font-size: 13px; }

  .brand-mark {
    position: absolute; left: 42px; top: 140px;
    display: flex; align-items: center; gap: 12px;
  }
  .brand-mark__square { width: 22px; height: 22px; background: var(--orange); }
  .brand-mark__name {
    color: var(--ink); font-weight: 600; font-size: 22px; letter-spacing: 6px;
  }

  .info-band {
    position: absolute; left: 0; right: 0; bottom: 0; height: 128px;
    background: linear-gradient(90deg, var(--orange-deep), var(--orange));
    color: var(--white);
    display: flex; justify-content: space-between;
    padding: 24px 34px 0 42px;
    font-size: 14px; line-height: 1.55;
  }
  .contact-list { list-style: none; }
  .contact-list li { display: flex; align-items: center; gap: 10px; }
  .contact-list svg { width: 14px; height: 14px; flex: none; }
  .address { text-align: right; font-style: normal; }

  /* brand side */
  .card--brand .brand-block {
    position: absolute; inset: 0;
    display: flex; flex-direction: column; align-items: center; justify-content: center; gap: 14px;
  }
  .card--brand .brand-mark { position: static; }
  .card--brand .brand-mark__square { width: 34px; height: 34px; }
  .card--brand .brand-mark__name { font-size: 34px; letter-spacing: 8px; color: var(--orange); }
  .tagline { color: var(--grey); font-style: italic; font-size: 17px; letter-spacing: 1px; }
</style>
</head>
<body>
<main class="canvas">

  <section class="card card--contact" aria-label="Contact side">
    <div class="corner-tab"></div>
    <div class="person">
      <p class="person__name">Luc Marchand</p>
      <p class="person__role">Director</p>
    </div>

    <div class="brand-mark">
      <span class="brand-mark__square"></span>
      <span class="brand-mark__name">Pellion</span>
    </div>

    <div class="info-band">
      <ul class="contact-list">
        <li>
          <svg viewBox="0 0 14 14" aria-hidden="true"><rect x="3" y="1" width="8" height="12" rx="1.5" fill="none" stroke="#fff" stroke-width="1.4"/><circle cx="7" cy="10.8" r="0.9" fill="#fff"/></svg>
          +44 7700 900 318
        </li>
        <li>
          <svg viewBox="0 0 14 14" aria-hidden="true"><rect x="1" y="3" width="12" height="8" fill="none" stroke="#fff" stroke-width="1.4"/><path d="M1 3l6 5 6-5" fill="none" stroke="#fff" stroke-width="1.4"/></svg>
          Luc.Marchand@pellion.gg
        </li>
        <li>
          <svg viewBox="0 0 14 14" aria-hidden="true"><circle cx="7" cy="7" r="5.8" fill="none" stroke="#fff" stroke-width="1.4"/><path d="M1.2 7h11.6M7 1.2c-2.4 3-2.4 8.6 0 11.6M7 1.2c2.4 3 2.4 8.6 0 11.6" fill="none" stroke="#fff" stroke-width="1"/></svg>
          www.pellion.gg
        </li>
      </ul>
      <address class="address">
        12 Rue des Pins, St Sampson<br>
        Guernsey, GY2 4QT<br>
        Channel Islands
      </address>
    </div>
  </section>

  <section class="card card--brand" aria-label="Brand side">
    <div class="brand-block">
      <div class="brand-mark">
        <span class="brand-mark__square"></span>
        <span class="brand-mark__name">Pellion</span>
      </div>
      <p class="tagline">Linking People</p>
    </div>
  </section>

</main>
</body>
</html>
```